First Reponders Promotion poster/flyer

Our Yoga studio is introducing an ongoing promotion for all First Responders, Police/Nurse/Paramedic/Firefighters/Doctors
$22pw for Unlimited access to our Inner city Studio which will become a sanctuary for the people who look after us. Tag line: You look after us, let us look after you. The benefits of yoga, reduce stress, clear mind, healthy body. Feel free to use other assets, and be as creative as you like I have just put images and designs as a guide.

Target Market(s)

Emergency Services Tasmania

Industry/Entity Type

Emergency Services

Requirements
Must have
• Stillwave Logo/Address 41 Marlow St/ website www.stillwavestudio.com.a/ sign up online and just bring in current work Id at checkin/$22pw Unlimited classes/Australian market so can't look like usa or any other countries
Nice to have
• words , inner city Sanctuary
Should not have
• Foreign Country images

```html
<!DOCTYPE html>
<html lang="en">
<head>
<meta charset="utf-8">
<title>Stillwave – First Responders Promo</title>
<link href="https://fonts.googleapis.com/css2?family=Montserrat:wght@300;400;500;600;700;800&display=swap" rel="stylesheet">
<style>
  :root{
    --gold:#f0aa24;
    --gold-soft:#fde7b0;
    --cream:#fff6e0;
    --ink:#161616;
    --grey-bg:#f4f4f5;
    --slate:#55585c;
    --label:#6b6d70;
    --crimson:#9c1f26;
    --page:#ececec;
    --white:#ffffff;
  }
  *{box-sizing:border-box;margin:0;padding:0}
  html,body{width:720px;height:1200px;overflow:hidden;background:var(--page);font-family:"Montserrat",sans-serif;color:var(--ink)}
  .flyer{position:absolute;left:0;top:132px;width:720px;height:935px;background:linear-gradient(180deg,#f7f7f8 0%,var(--grey-bg) 100%);box-shadow:0 6px 14px rgba(0,0,0,.25);overflow:hidden}

  .hero{position:absolute;left:0;top:0;width:720px;height:342px;background:linear-gradient(180deg,#fff3d6 0%,var(--gold-soft) 100%)}
  .brand{position:absolute;left:51px;top:44px;font-size:17px;font-weight:500;letter-spacing:8px;color:var(--ink)}
  .headline{position:absolute;left:51px;top:140px;z-index:2;font-weight:400;font-size:27px;line-height:31px;letter-spacing:-.3px;color:var(--ink)}
  .headline .accent{color:var(--gold);font-weight:700;display:block;font-size:29px}
  .headline .line{display:block}
  .headline .gap{margin-top:12px}
  .headline .bang{color:var(--crimson);font-weight:700}
  .emblem{position:absolute;left:350px;top:48px;width:318px;height:294px;border-radius:50% 50% 0 0;background:radial-gradient(circle at 50% 65%,#fde2b0 0%,#f6b544 35%,#e99a1d 48%,#a3232a 62%,#8e1b21 100%)}

  .promo-title{position:absolute;left:0;width:720px;top:356px;text-align:center;font-size:31px;font-weight:800;letter-spacing:.3px}
  .promo-title .accent{color:var(--gold)}
  .offer{position:absolute;left:103px;top:408px;display:flex;height:54px}
  .offer-text{width:386px;background:var(--slate);color:var(--white);font-size:17px;font-weight:600;line-height:23px;padding:4px 7px}
  .offer-price{width:128px;background:var(--white);border:1px solid var(--slate);display:flex;align-items:flex-end;justify-content:center;padding-bottom:3px;font-weight:700}
  .offer-price .cur{color:var(--gold);font-size:18px;align-self:flex-start;margin-top:6px}
  .offer-price .amt{color:var(--gold);font-size:40px;line-height:40px}
  .offer-price .per{font-size:22px;line-height:26px}

  .benefits{position:absolute;left:51px;top:492px;width:280px;height:168px}
  .benefits-icon{position:absolute;left:0;top:4px}
  .benefits h2{position:absolute;left:51px;top:0;font-size:20px;font-weight:700;line-height:22px}
  .benefits h2 .accent{display:block;color:var(--gold);font-weight:400;font-size:31px;line-height:32px}
  .bracket{position:absolute;left:0;top:0}
  .benefit-list{position:absolute;left:35px;top:70px;list-style:none}
  .benefit-list li{display:flex;align-items:center;height:29px;font-size:17px;font-weight:700}
  .benefit-list .chip{width:19px;height:19px;background:var(--gold);margin-right:20px;display:flex;align-items:center;justify-content:center}

  .signup{position:absolute;left:51px;top:680px;font-size:12.5px;font-weight:600;line-height:19px}
  .signup .accent{color:var(--gold);font-size:16.5px;font-weight:700}
  .signup .web{display:inline-block;margin-top:4px;color:var(--slate);font-weight:600;font-size:12.5px}

  .faq{position:absolute;left:343px;top:492px;width:377px;height:127px;background:var(--white);box-shadow:0 1px 5px rgba(0,0,0,.12)}
  .faq .mark{position:absolute;left:14px;top:6px;font-size:46px;font-weight:800;color:var(--gold)}
  .faq h2{position:absolute;left:57px;top:6px;font-size:21px;font-weight:700;line-height:22px}
  .faq h2 .accent{display:block;color:var(--gold);font-weight:400;font-size:27px;line-height:30px}
  .faq dl{position:absolute;left:23px;top:76px;font-size:13.5px;line-height:26px}
  .faq dt,.faq dd{display:inline}
  .faq .q{color:var(--slate);font-weight:600}
  .faq .qtext{margin-left:18px;font-weight:500;color:var(--slate)}
  .faq .a{font-weight:700}
  .faq .atext{color:var(--slate);font-weight:500;margin-left:4px}

  .when-where{position:absolute;right:53px;top:660px;text-align:right}
  .when{font-size:16px;font-weight:400;line-height:36px;border-bottom:1px solid #9a9a9a;padding-bottom:2px}
  .when .date{color:var(--gold);font-size:31px;font-weight:700}
  .when .year{font-size:31px;font-weight:700}
  .where{font-size:27px;font-weight:700;line-height:38px}
  .where .accent{color:var(--gold)}

  .responders{position:absolute;left:51px;top:782px;display:flex;gap:13px;list-style:none}
  .responders li{width:77px;text-align:center}
  .responders .photo{width:77px;height:72px;border:2px solid var(--gold)}
  .responders .label{margin-top:12px;font-size:11px;font-weight:500;color:var(--label);white-space:nowrap;margin-left:-6px;margin-right:-6px}
  .footer-bar{position:absolute;left:0;bottom:0;width:720px;height:16px;background:#5f6165}
</style>
</head>
<body>
<main class="flyer">
  <section class="hero">
    <div class="brand">STILLWAVE</div>
    <div class="emblem" role="img" aria-label="Crimson lotus emblem with glowing golden rings around a seated meditating figure"></div>
    <h1 class="headline">
      <span class="accent">YOU</span>
      <span class="line">LOOK AFTER US</span>
      <span class="accent gap">LET US</span>
      <span class="line">LOOK AFTER YOU<span class="bang">!</span></span>
    </h1>
  </section>

  <h2 class="promo-title"><span class="accent">FIRST RESPONDERS</span> PROMO</h2>
  <div class="offer">
    <p class="offer-text">Unlimited access to our classes in our beautiful inner-city Studio Sanctuary for</p>
    <p class="offer-price"><span class="cur">$</span><span class="amt">22</span><span class="per">PW</span></p>
  </div>

  <section class="benefits">
    <svg class="bracket" width="280" height="168" viewBox="0 0 280 168">
      <polyline points="222,44 250,44 250,164 16,164" fill="none" stroke="#f0aa24" stroke-width="2"/>
      <line x1="8" y1="164" x2="28" y2="164" stroke="#f0aa24" stroke-width="6" stroke-linecap="round"/>
    </svg>
    <svg class="benefits-icon" width="40" height="44" viewBox="0 0 40 44">
      <g fill="#f0aa24">
        <circle cx="20" cy="16" r="7"/>
        <ellipse cx="20" cy="4" rx="3" ry="5"/>
        <ellipse cx="8" cy="10" rx="3" ry="5" transform="rotate(-50 8 10)"/>
        <ellipse cx="32" cy="10" rx="3" ry="5" transform="rotate(50 32 10)"/>
        <ellipse cx="4" cy="22" rx="3" ry="5" transform="rotate(-90 4 22)"/>
        <ellipse cx="36" cy="22" rx="3" ry="5" transform="rotate(90 36 22)"/>
        <rect x="17" y="24" width="6" height="14"/>
        <rect x="11" y="38" width="18" height="4" rx="2"/>
      </g>
    </svg>
    <h2>BENEFITS <span class="accent">OF YOGA</span></h2>
    <ul class="benefit-list">
      <li><span class="chip"><svg width="11" height="11" viewBox="0 0 11 11"><circle cx="5.5" cy="5.5" r="4.5" fill="#161616"/></svg></span>REDUCE STRESS</li>
      <li><span class="chip"><svg width="11" height="11" viewBox="0 0 11 11"><circle cx="5.5" cy="5.5" r="4.5" fill="none" stroke="#161616" stroke-width="2"/></svg></span>CLEAR MIND</li>
      <li><span class="chip"><svg width="11" height="11" viewBox="0 0 11 11"><path d="M5.5 1v9M1.5 4h8" stroke="#161616" stroke-width="2"/></svg></span>HEALTHY BODY</li>
    </ul>
  </section>

  <p class="signup">Just <span class="accent">SIGN UP ON WEBSITE</span><br>and bring in your <span class="accent">CURRENT ID</span><br>for verification.<br><span class="web">www.stillwavestudio.com.a</span></p>

  <aside class="faq">
    <span class="mark">?</span>
    <h2>QUESTIONS <span class="accent">THEY MIGHT HAVE</span></h2>
    <dl>
      <dt class="q">Q:</dt><dd class="qtext">IS THERE ANY CONTRACT?</dd><br>
      <dt class="a">Ans:</dt><dd class="atext">No only email 2 weeks prior to cancel.</dd>
    </dl>
  </aside>

  <div class="when-where">
    <p class="when">Starts From <span class="date">July 1,</span> <span class="year">2022</span></p>
    <p class="where"><span class="accent">41 Marlow St,</span> Hobart</p>
  </div>

  <ul class="responders">
    <li><div class="photo" role="img" aria-label="Police officer in high-visibility vest" style="background:linear-gradient(160deg,#2f3a4a,#b7b23a)"></div><p class="label">POLICE</p></li>
    <li><div class="photo" role="img" aria-label="Ambulance crew member at work" style="background:linear-gradient(160deg,#e7ecef,#8fa3b4)"></div><p class="label">AMBULANCE</p></li>
    <li><div class="photo" role="img" aria-label="Paramedic treating a patient" style="background:linear-gradient(160deg,#6b4a3a,#c9432e)"></div><p class="label">PARAMEDIC</p></li>
    <li><div class="photo" role="img" aria-label="Nurse holding a clipboard" style="background:linear-gradient(160deg,#f2f4f6,#5aa0d6)"></div><p class="label">NURSE</p></li>
    <li><div class="photo" role="img" aria-label="Firefighter in protective gear" style="background:linear-gradient(160deg,#1f2226,#5b5a4a)"></div><p class="label">FIRE FIGHTER</p></li>
    <li><div class="photo" role="img" aria-label="Emergency services worker studying a map" style="background:linear-gradient(160deg,#4a4036,#c8bfae)"></div><p class="label">SES</p></li>
    <li><div class="photo" role="img" aria-label="Doctor consulting with a patient" style="background:linear-gradient(160deg,#dfe7ee,#6f93b8)"></div><p class="label">DOCTOR</p></li>
  </ul>

  <div class="footer-bar"></div>
</main>
</body>
</html>
```